ashby paving works

Needs to have phone number 0412885107 and email marklowry@pavemail.com.au.
ABN 27613048852
name mark lowry

For all your concreting solutions
Excavation
Exposed & colour concrete
House & shed slabs
Driveways
Landing & steps

Contact Information for Business Card

ph 0412885107
email marklowry@pavemail.com.au.
ABN 27613048852
name mark lowry

```html
<!DOCTYPE html>
<html lang="en">
<head>
<meta charset="utf-8">
<title>Ashby Paving Works — Business Card</title>
<link rel="stylesheet" href="https://fonts.googleapis.com/css2?family=Raleway:wght@400;500;700;800&display=swap">
<style>
  :root {
    --orange: #e96a22;
    --slate: #6a6a6a;
    --slate-dark: #5c5c5c;
    --ink: #555555;
    --paper: #ffffff;
    --stage: #e9e7e3;
    --faint: rgba(255,255,255,0.07);
  }
  * { margin: 0; padding: 0; box-sizing: border-box; }
  html, body { width: 1200px; height: 886px; overflow: hidden; }
  body {
    background: var(--stage);
    font-family: "Raleway", sans-serif;
    display: flex;
    align-items: center;
    justify-content: center;
    gap: 48px;
  }
  .card {
    width: 540px;
    height: 310px;
    position: relative;
    overflow: hidden;
    box-shadow: 0 10px 28px rgba(0,0,0,0.18);
  }

  /* ---------- front ---------- */
  .card--front { background: var(--paper); }
  .brand-panel {
    position: absolute;
    left: 28px; top: 0; bottom: 0;
    width: 190px;
  }
  .brand-panel__top { position: absolute; inset: 0 0 50% 0; background: var(--slate); }
  .brand-panel__bottom { position: absolute; inset: 50% 0 0 0; background: var(--orange); }
  .brand-mark {
    position: absolute;
    left: 0; right: 0; top: 50%;
    transform: translateY(-50%);
    display: flex; align-items: center; justify-content: center; gap: 8px;
    color: var(--paper);
    font-weight: 800;
    font-size: 15px;
    letter-spacing: 0.08em;
    text-transform: uppercase;
  }
  .brand-mark__square { width: 10px; height: 10px; background: var(--paper); }

  .front-details {
    position: absolute;
    left: 250px; top: 34px; right: 24px;
  }
  .company { display: inline-block; text-align: center; }
  .company__name {
    color: var(--orange); font-weight: 700; font-size: 19px;
    text-transform: uppercase; letter-spacing: 0.02em;
  }
  .company__sub {
    display: flex; align-items: center; gap: 8px;
    color: var(--ink); font-weight: 500; font-size: 15px;
    letter-spacing: 0.14em; text-transform: uppercase; margin-top: 1px;
  }
  .company__sub::before, .company__sub::after {
    content: ""; flex: 1; height: 2px; background: var(--slate);
  }
  .company__phone { color: var(--orange); font-size: 15px; font-weight: 500; letter-spacing: 0.04em; }

  .person {
    margin-top: 26px;
    color: var(--orange); font-weight: 800; font-size: 19px; text-transform: uppercase;
  }
  .contact-list { list-style: none; margin-top: 12px; }
  .contact-list li {
    display: flex; align-items: center; gap: 8px;
    color: var(--ink); font-size: 12.5px; line-height: 21px;
  }
  .contact-list svg { width: 11px; height: 11px; fill: var(--orange); flex: none; }
  .contact-list .abn { padding-left: 0; margin-top: 2px; }

  /* ---------- back ---------- */
  .card--back { background: linear-gradient(135deg, var(--slate) 0%, var(--slate-dark) 100%); }
  .back-watermark {
    position: absolute; left: 0; right: 0; top: 52px;
    text-align: center;
    color: var(--faint);
    font-weight: 800; font-size: 46px; letter-spacing: 0.06em; text-transform: uppercase;
  }
  .back-company {
    position: absolute; left: 30px; bottom: 70px; text-align: center;
  }
  .back-company .company__sub { color: var(--paper); }
  .back-company .company__sub::before, .back-company .company__sub::after { background: var(--paper); }
  .back-web {
    position: absolute; left: 30px; bottom: 34px;
    color: var(--paper); font-size: 12px; letter-spacing: 0.42em;
  }
  .services {
    position: absolute; right: 28px; bottom: 34px;
    list-style: none; text-align: right;
  }
  .services li {
    color: var(--paper); font-size: 13px; line-height: 22px;
    display: flex; align-items: center; justify-content: flex-end; gap: 8px;
  }
  .services li::after {
    content: ""; width: 5px; height: 5px; border-radius: 50%; background: var(--orange);
  }
</style>
</head>
<body>

<section class="card card--front" aria-label="Business card front">
  <div class="brand-panel">
    <div class="brand-panel__top"></div>
    <div class="brand-panel__bottom"></div>
    <div class="brand-mark"><span class="brand-mark__square"></span>Ashby Paving Works</div>
  </div>

  <div class="front-details">
    <div class="company">
      <div class="company__name">Ashby Paving</div>
      <div class="company__sub">Works</div>
      <div class="company__phone">0412885107</div>
    </div>

    <div class="person">Mark Lowry</div>

    <ul class="contact-list">
      <li>
        <svg viewBox="0 0 24 24" aria-hidden="true"><path d="M6.6 10.8a15 15 0 0 0 6.6 6.6l2.2-2.2c.3-.3.7-.4 1-.2 1.1.4 2.3.6 3.6.6.6 0 1 .4 1 1V20c0 .6-.4 1-1 1C10.6 21 3 13.4 3 4c0-.6.4-1 1-1h3.5c.6 0 1 .4 1 1 0 1.3.2 2.5.6 3.6.1.3 0 .7-.2 1z"/></svg>
        0412885107
      </li>
      <li>
        <svg viewBox="0 0 24 24" aria-hidden="true"><path d="M2 5h20v14H2z M2 5l10 7 10-7" /></svg>
        marklowry@pavemail.com.au
      </li>
      <li>
        <svg viewBox="0 0 24 24" aria-hidden="true"><circle cx="12" cy="12" r="10"/></svg>
        www.ashbypaving.com.au
      </li>
      <li class="abn">ABN 27613048852</li>
    </ul>
  </div>
</section>

<section class="card card--back" aria-label="Business card back">
  <div class="back-watermark">Ashby Paving Works</div>

  <div class="back-company company">
    <div class="company__name">Ashby Paving</div>
    <div class="company__sub">Works</div>
    <div class="company__phone">0412885107</div>
  </div>
  <div class="back-web">www.ashbypaving.com.au</div>

  <ul class="services">
    <li>Excavation</li>
    <li>Exposed &amp; colour concrete</li>
    <li>House &amp; shed slabs</li>
    <li>Driveways</li>
    <li>Landing &amp; steps</li>
  </ul>
</section>

</body>
</html>
```